Law Firm Letterhead

We are looking for a letterhead for our military/veterans law firm. We like simplicity and clean, modern, flat, uncluttered designs. Our logo font is DIN 1451, and our website/business card info font is Helvetica Neue.

Required Information:

- Logo/Graphic: Please see attached logo / business card for ideas. Please also review firm website.

- Motto: A law firm for service members and veterans

- Web Address: www.brightharborcounsel.example

- Email: info@brightharborcounsel.example

- Phone: 866-214-3097

Colors: We prefer either a blue/grey or an all-blue color scheme. The blue in our logo is #336699.

Please DO NOT submit more than 3 designs. Spamming designs with only minor changes between the designs is not appreciated. We can evaluate your quality and direction by your best 1 or 2 designs.

Thank you!

```html
<!DOCTYPE html>
<html lang="en">
<head>
<meta charset="utf-8">
<title>Bright Harbor Counsel — Letterhead</title>
<link rel="stylesheet" href="https://fonts.googleapis.com/css2?family=Barlow+Semi+Condensed:wght@600&family=Jost:wght@400;500&display=swap">
<style>
  :root {
    --backdrop: #e4e4e4;
    --paper: #ffffff;
    --brand-blue: #2a66c9;
    --mark-tint: #e8eef8;
    --ink: #111111;
  }
  html, body {
    margin: 0;
    padding: 0;
    width: 961px;
    height: 1200px;
    overflow: hidden;
    background: var(--backdrop);
  }
  .letterhead {
    position: absolute;
    left: 80px;
    top: 95px;
    width: 812px;
    height: 1050px;
    background: var(--paper);
    box-shadow: 0 2px 6px rgba(0,0,0,0.15);
  }
  .brand-square {
    position: absolute;
    left: 24px;
    top: 18px;
    width: 68px;
    height: 68px;
    background: var(--brand-blue);
  }
  .firm-name {
    position: absolute;
    left: 104px;
    top: 16px;
    margin: 0;
    font-family: "Barlow Semi Condensed", "Roboto Condensed", sans-serif;
    font-weight: 600;
    font-size: 34px;
    line-height: 36px;
    letter-spacing: 0.5px;
    color: var(--brand-blue);
    text-transform: uppercase;
  }
  .contact {
    position: absolute;
    left: 104px;
    top: 102px;
    margin: 0;
    font-family: "Jost", "Helvetica Neue", sans-serif;
    font-weight: 500;
    font-size: 14.5px;
    line-height: 22px;
    color: var(--ink);
  }
  .contact .label { color: var(--brand-blue); }
  .watermark {
    position: absolute;
    left: 244px;
    top: 547px;
    width: 325px;
    height: 325px;
    background: var(--mark-tint);
  }
  .footer {
    position: absolute;
    left: 0;
    right: 0;
    top: 997px;
    text-align: center;
    font-family: "Jost", "Helvetica Neue", sans-serif;
    color: var(--ink);
  }
  .motto {
    margin: 0;
    font-size: 17px;
    font-weight: 500;
    letter-spacing: 0.8px;
    line-height: 22px;
  }
  .web {
    margin: 2px 0 0;
    font-size: 14.5px;
    font-weight: 400;
    line-height: 20px;
  }
</style>
</head>
<body>
  <main class="letterhead">
    <div class="brand-square"></div>
    <h1 class="firm-name">Bright Harbor<br>Counsel</h1>
    <p class="contact">
      <span class="label">p:</span> 866-214-3097<br>
      <span class="label">e:</span> info@brightharborcounsel.example
    </p>
    <div class="watermark"></div>
    <footer class="footer">
      <p class="motto">A law firm for service members and veterans</p>
      <p class="web">www.brightharborcounsel.example</p>
    </footer>
  </main>
</body>
</html>
```